low rate guarantee

newspaper ad

Target Market(s)

homeowners

Industry/Entity Type

Finance

Font styles to use
Sans Serif

Colors
f78f20

Requirements
Must have
• Pellby Home Loans logo
• low rate - guarantee (logo)
• How low can you go?
• The lowest. Guaranteed.
Nice to have
• With our lowest rate guarantee program, if you find a lower rate than ours we'll beat it or pay you $500.

```html
<!DOCTYPE html>
<html lang="en">
<head>
<meta charset="utf-8">
<title>Pellby Home Loans – Lowest Rate Guarantee</title>
<link rel="stylesheet" href="https://fonts.googleapis.com/css2?family=Saira:wght@400;500;700;800&family=Lora:ital@1&display=swap">
<style>
  :root {
    --brand-orange: #f78f20;
    --ink: #2b2522;
    --white: #ffffff;
    --footer-bg: #2a2a2a;
    --gold-light: #f6d46a;
    --gold-dark: #c8901c;
    --dash: rgba(255,255,255,0.85);
  }
  html, body { margin: 0; padding: 0; overflow: hidden; background: #ffffff; }
  .ad {
    position: relative;
    width: 674px;
    height: 1200px;
    background: var(--brand-orange);
    font-family: "Saira", sans-serif;
    color: var(--white);
    overflow: hidden;
  }
  .brand {
    position: absolute;
    left: 64px;
    top: 58px;
    width: 540px;
    height: 100px;
  }
  .brand-mark {
    position: absolute;
    left: 14px;
    top: 24px;
    width: 54px;
    height: 54px;
    border-radius: 50%;
    background: var(--ink);
  }
  .brand-name {
    position: absolute;
    left: 100px;
    top: 8px;
    margin: 0;
    font-size: 46px;
    font-weight: 700;
    letter-spacing: -0.3px;
    line-height: 1;
    color: var(--ink);
    white-space: nowrap;
  }
  .brand-tagline {
    position: absolute;
    right: 6px;
    top: 78px;
    font-family: "Lora", serif;
    font-style: italic;
    font-size: 17px;
    color: var(--ink);
  }
  .guarantee-seal {
    position: absolute;
    left: 212px;
    top: 228px;
    width: 246px;
    height: 246px;
  }
  .divider {
    position: absolute;
    left: 64px;
    width: 544px;
    border-top: 2px dashed var(--dash);
  }
  .divider--top { top: 510px; }
  .divider--bottom { top: 700px; }
  .headline {
    position: absolute;
    left: 0;
    width: 100%;
    margin: 0;
    text-align: center;
    line-height: 1;
  }
  .headline--strong { top: 536px; font-size: 60px; font-weight: 800; letter-spacing: 1px; }
  .headline--light { top: 606px; font-size: 52px; font-weight: 400; letter-spacing: 3px; }
  .promise {
    position: absolute;
    top: 740px;
    left: 0;
    width: 100%;
    margin: 0;
    text-align: center;
    font-size: 60px;
    font-weight: 800;
    line-height: 68px;
  }
  .offer {
    position: absolute;
    top: 901px;
    left: 0;
    width: 100%;
    margin: 0;
    text-align: center;
    font-size: 26px;
    letter-spacing: 0.6px;
    line-height: 31px;
    color: var(--ink);
  }
  .offer strong { font-weight: 800; }
  .offer-payout {
    display: block;
    margin-top: 3px;
    font-size: 32px;
    font-weight: 800;
    letter-spacing: 1px;
  }
  .contact-bar {
    position: absolute;
    left: 0;
    bottom: 0;
    width: 100%;
    height: 96px;
    background: var(--footer-bg);
  }
  .contact-item {
    position: absolute;
    top: 50%;
    transform: translateY(-50%);
    display: flex;
    align-items: center;
    gap: 8px;
    font-weight: 800;
    color: var(--white);
    white-space: nowrap;
  }
  .contact-item--phone { left: 22px; font-size: 28px; letter-spacing: 1px; }
  .contact-item--email { left: 320px; font-size: 25px; letter-spacing: 0.5px; }
  .contact-icon { flex: none; }
</style>
</head>
<body>
  <main class="ad">
    <header class="brand">
      <span class="brand-mark" aria-hidden="true"></span>
      <h1 class="brand-name">Pellby Home Loans</h1>
      <span class="brand-tagline">Home made simple.</span>
    </header>

    <svg class="guarantee-seal" viewBox="0 0 246 246" role="img" aria-label="Lowest rate guarantee badge">
      <defs>
        <radialGradient id="sealGold" cx="40%" cy="35%" r="70%">
          <stop offset="0%" stop-color="var(--gold-light)"/>
          <stop offset="100%" stop-color="var(--gold-dark)"/>
        </radialGradient>
      </defs>
      <circle cx="123" cy="123" r="122" fill="url(#sealGold)"/>
    </svg>

    <div class="divider divider--top"></div>
    <h2 class="headline headline--strong">HOW LOW</h2>
    <p class="headline headline--light">can you go?</p>
    <div class="divider divider--bottom"></div>

    <p class="promise">The lowest<br>Guaranteed!!!</p>

    <p class="offer">
      With our <strong>lowest rate guarantee program,</strong><br>
      if you find a lower rate than ours<br>
      we'll beat it or
      <span class="offer-payout">pay you $500.</span>
    </p>

    <footer class="contact-bar">
      <span class="contact-item contact-item--phone">
        <svg class="contact-icon" width="26" height="26" viewBox="0 0 24 24" aria-hidden="true">
          <path fill="var(--brand-orange)" d="M6.6 10.8c1.4 2.8 3.8 5.1 6.6 6.6l2.2-2.2c.3-.3.7-.4 1-.2 1.1.4 2.3.6 3.6.6.6 0 1 .4 1 1V20c0 .6-.4 1-1 1C10.6 21 3 13.4 3 4c0-.6.4-1 1-1h3.5c.6 0 1 .4 1 1 0 1.3.2 2.5.6 3.6.1.3 0 .7-.2 1z"/>
        </svg>
        (321) 0102020
      </span>
      <span class="contact-item contact-item--email">
        <svg class="contact-icon" width="28" height="20" viewBox="0 0 28 20" aria-hidden="true">
          <rect x="1" y="1" width="26" height="18" fill="none" stroke="var(--brand-orange)" stroke-width="2"/>
          <path d="M1 1l13 10L27 1M1 19l10-9M27 19l-10-9" fill="none" stroke="var(--brand-orange)" stroke-width="2"/>
        </svg>
        hello@pellbyloans.com
      </span>
    </footer>
  </main>
</body>
</html>
```